8 Page Cheerleading Brochure, promoting travel options

Creation of an 8 Page A4 Brochure, portrait layout and print ready. To promote Cheerleading travel options and services to cheer gyms.
Front page to feature cheer image
Pages to include destination images and hotel images.

Colors
e34197
ec1f27

```html
<!DOCTYPE html>
<html lang="en">
<head>
<meta charset="utf-8">
<title>Meridian Tours – Cheer Travel Brochure</title>
<link href="https://fonts.googleapis.com/css2?family=Roboto:wght@400;700&family=Lato:wght@400&display=swap" rel="stylesheet">
<style>
  :root{
    --pink:#e34197;
    --red:#ec1f27;
    --ink:#2a2a2a;
    --bg:#ece9e6;
    --paper:#ffffff;
    --grey-a:#f2f2f2;
    --grey-b:#dcdcdc;
    --badge:#c9c9c9;
  }
  *{box-sizing:border-box;margin:0;padding:0}
  html,body{width:1200px;height:1200px;overflow:hidden;background:var(--bg)}
  body{position:relative;font-family:'Roboto',sans-serif;color:var(--ink)}
  .page{position:absolute;width:364px;height:514px;background:var(--paper);overflow:hidden;box-shadow:0 2px 10px rgba(0,0,0,.18)}
  .page--front{left:50px;top:82px}
  .page--back{left:751px;top:82px;background:linear-gradient(150deg,var(--grey-a) 0%,#e6e6e6 45%,var(--grey-b) 100%)}
  .page--inside{left:414px;top:654px;background:linear-gradient(155deg,#f4f4f4 0%,#e9e9e9 55%,#dedede 100%)}
  .abs{position:absolute}
  .brand-name{position:absolute;display:flex;align-items:center;gap:6px;font-family:'Roboto',sans-serif;font-weight:700;color:var(--ink);white-space:nowrap;letter-spacing:.3px}
  .brand-name::before{content:"";width:.7em;height:.7em;border-radius:50%;background:var(--ink)}
  .pink-rule{position:absolute;background:var(--pink)}
  .photo{position:absolute}

  /* front */
  .front-photo{left:0;top:0;width:184px;height:450px;background:linear-gradient(180deg,#1e1a24 0%,#5a3a3a 40%,#b3877a 70%,#3a2a2a 100%)}
  .front-band{left:186px;top:184px;width:178px;height:116px;background:var(--pink);color:#fff;padding:22px 0 0 20px}
  .front-band .t1{font-weight:700;font-size:39px;line-height:37px;letter-spacing:.5px}
  .front-band .t2{font-weight:400;font-size:39px;line-height:37px;letter-spacing:.5px}
  .partner-badge{left:218px;top:376px;width:54px;height:54px;border-radius:50%;background:var(--badge)}
  .contact-row{position:absolute;left:12px;right:16px;top:480px;display:flex;justify-content:space-between;font-family:'Lato',sans-serif;font-size:8px;color:#333;align-items:center}
  .contact-row span,.contact-list li{display:flex;align-items:center;gap:5px}
  .footer-line{position:absolute;left:17px;right:17px;top:496px;height:1px;background:#888}

  /* back */
  .back-photo{left:202px;top:0;width:162px;height:485px;background:linear-gradient(180deg,#3d3530 0%,#8a6a55 22%,#c99e7e 45%,#b88a6b 100%)}
  .contact-list{position:absolute;left:17px;list-style:none;font-family:'Lato',sans-serif;font-size:8px;line-height:11px;color:#333}

  /* inside */
  .heading{left:17px;top:18px;font-weight:700;font-size:12px;color:var(--red);border-bottom:1px solid var(--red);padding-bottom:1px}
  .body-copy{font-size:8.4px;line-height:11px;color:#333;text-align:justify}
  .inside-photo{left:17px;top:153px;width:144px;height:341px;background:linear-gradient(180deg,#5c9fe0 0%,#a9cdee 30%,#6f8a5a 52%,#3cc9dc 62%,#2aa6c6 100%)}
  .callout{left:0;top:219px;width:133px;height:76px;background:var(--red);color:#fff;font-size:8.6px;line-height:11.8px;padding:8px 10px 0 16px}
  .services{position:absolute;left:184px;top:316px;width:165px;list-style:none;font-size:8.4px;line-height:11px;color:#333}
  .services li{display:flex;gap:7px;margin-bottom:4px}
  .services svg{flex:none;margin-top:1px}
</style>
</head>
<body>

<section class="page page--front">
  <div class="photo front-photo" role="img" aria-label="Cheerleading team in red and navy uniforms with hair bows, gathered on stage"></div>
  <div class="pink-rule" style="left:186px;top:88px;width:3px;height:363px"></div>
  <div class="pink-rule" style="left:61px;top:448px;width:128px;height:4px"></div>
  <div class="brand-name" style="left:208px;top:78px;font-size:19px">Meridian Tours</div>
  <div class="abs front-band"><div class="t1">CHEER</div><div class="t2">TRAVEL</div></div>
  <div class="abs partner-badge" role="img" aria-label="Partner federation badge"></div>
  <div class="contact-row">
    <span><svg width="8" height="7" viewBox="0 0 8 7"><path d="M0 2 Q4 -1 8 2 L7 3 L5 2 L3 2 L1 3 Z M1 4 H7 V7 H1 Z" fill="#333"/></svg>(02) 5550 1234</span>
    <span><svg width="7" height="7" viewBox="0 0 7 7"><circle cx="3.5" cy="3.5" r="3" fill="none" stroke="#333"/><path d="M0.5 3.5H6.5M3.5 0.5V6.5" stroke="#333" stroke-width=".7"/></svg>www.meridiantours.travel</span>
    <span><svg width="6" height="8" viewBox="0 0 6 8"><path d="M3 8 L0.5 4 A2.7 2.7 0 1 1 5.5 4 Z" fill="#333"/><circle cx="3" cy="3" r="1" fill="#fff"/></svg>hello@meridiantours.travel</span>
  </div>
  <div class="footer-line"></div>
</section>

<section class="page page--back">
  <div class="photo back-photo" role="img" aria-label="Pink orchid lei laid in a heart shape on beach sand"></div>
  <div class="pink-rule" style="left:198px;top:0;width:4px;height:490px"></div>
  <div class="pink-rule" style="left:198px;top:486px;width:128px;height:4px"></div>
  <div class="brand-name" style="left:16px;top:254px;font-size:19px">Meridian Tours</div>
  <ul class="contact-list" style="top:456px">
    <li><svg width="7" height="6" viewBox="0 0 8 7"><path d="M0 2 Q4 -1 8 2 L7 3 L5 2 L3 2 L1 3 Z M1 4 H7 V7 H1 Z" fill="#333"/></svg>(02) 5550 1234</li>
    <li><svg width="6" height="6" viewBox="0 0 7 7"><circle cx="3.5" cy="3.5" r="3" fill="none" stroke="#333"/><path d="M0.5 3.5H6.5M3.5 0.5V6.5" stroke="#333" stroke-width=".7"/></svg>www.meridiantours.travel</li>
    <li><svg width="5" height="7" viewBox="0 0 6 8"><path d="M3 8 L0.5 4 A2.7 2.7 0 1 1 5.5 4 Z" fill="#333"/><circle cx="3" cy="3" r="1" fill="#fff"/></svg>hello@meridiantours.travel</li>
  </ul>
  <div class="footer-line" style="background:#999"></div>
</section>

<section class="page page--inside">
  <h2 class="abs heading">ABOUT US</h2>
  <p class="abs body-copy" style="left:17px;top:56px;width:331px">Meridian Tours was established in 2001, originally specialising in Basketball Tours and quickly expanding to provide a variety of other sports options including cheerleading. Our customers have enjoyed destinations including the USA, Canada, China, Singapore, Vietnam, Europe, UK, South Africa, New Zealand and Australia.</p>
  <p class="abs body-copy" style="left:17px;top:122px;width:331px">Meridian are the official Travel Partner of the National Cheer Alliance.</p>
  <div class="photo inside-photo" role="img" aria-label="Resort swimming pool with turquoise water under a blue sky"></div>
  <p class="abs callout">Meridian’s passion and mission remains to provide ‘once in a lifetime’ experiences to all of our valued customers.</p>
  <p class="abs body-copy" style="left:184px;top:159px;width:165px">Our understanding of the unique requirements of group travel and our personalised approach makes us the ideal choice in planning, sourcing and managing the perfect tour for your school or club. Our ever-growing global network allows us to offer exclusive experiences that are inaccessible to others. Our dedicated Tour Coordinators thoroughly consult with teaches and coaches to tailor an itinerary and tour management plan that meets each unique set of requirements. We can assist in providing:</p>
  <ul class="services">
    <li><svg width="9" height="9" viewBox="0 0 10 10"><circle cx="5" cy="5" r="5" fill="var(--red)"/><path d="M2.6 5.2 L4.4 7 L7.6 3.4" stroke="#fff" stroke-width="1.4" fill="none"/></svg>Customised Itineraries</li>
    <li><svg width="9" height="9" viewBox="0 0 10 10"><circle cx="5" cy="5" r="5" fill="var(--red)"/><path d="M2.6 5.2 L4.4 7 L7.6 3.4" stroke="#fff" stroke-width="1.4" fill="none"/></svg>Group Payment Plans</li>
    <li><svg width="9" height="9" viewBox="0 0 10 10"><circle cx="5" cy="5" r="5" fill="var(--red)"/><path d="M2.6 5.2 L4.4 7 L7.6 3.4" stroke="#fff" stroke-width="1.4" fill="none"/></svg>Trusted, Quality Suppliers</li>
    <li><svg width="9" height="9" viewBox="0 0 10 10"><circle cx="5" cy="5" r="5" fill="var(--red)"/><path d="M2.6 5.2 L4.4 7 L7.6 3.4" stroke="#fff" stroke-width="1.4" fill="none"/></svg><span>Negotiated Group Discounts on airfares, accommodation, transport and activities</span></li>
  </ul>
  <div class="brand-name" style="left:184px;top:446px;font-size:12px">Meridian Tours</div>
  <ul class="contact-list" style="left:184px;top:468px">
    <li><svg width="6" height="6" viewBox="0 0 7 7"><circle cx="3.5" cy="3.5" r="3" fill="none" stroke="#333"/><path d="M0.5 3.5H6.5M3.5 0.5V6.5" stroke="#333" stroke-width=".7"/></svg>www.meridiantours.travel</li>
    <li><svg width="5" height="7" viewBox="0 0 6 8"><path d="M3 8 L0.5 4 A2.7 2.7 0 1 1 5.5 4 Z" fill="#333"/><circle cx="3" cy="3" r="1" fill="#fff"/></svg>hello@meridiantours.travel</li>
  </ul>
  <div class="pink-rule" style="left:17px;right:17px;top:495px;height:2px"></div>
</section>

</body>
</html>
```